Business card design for Tolvin Waste

I would like double-sided business cards for myself and my partner that includes our logo and the existing colour scheme. We provide waste and environmental services to customers in the motor-vehicle and engineering industries.

```html
<!DOCTYPE html>
<html lang="en">
<head>
<meta charset="utf-8">
<title>Tolvin Waste – Business Card</title>
<link rel="stylesheet" href="https://fonts.googleapis.com/css2?family=Roboto:wght@400;500;700&display=swap">
<style>
  :root {
    --backdrop: #efede9;
    --kraft: #d8d5d0;
    --ink: #4a4a4c;
    --leaf-green: #4caf3f;
    --lime: #b9dc3c;
    --lime-text: #cfe84a;
    --white: #ffffff;
    --icon-disc: #9fd068;
    --icon-glyph: #2f6f25;
  }
  * { box-sizing: border-box; margin: 0; padding: 0; }
  html, body { width: 1200px; height: 800px; overflow: hidden; }
  body {
    background: var(--backdrop);
    font-family: "Roboto", Arial, sans-serif;
    position: relative;
  }
  .card {
    position: absolute;
    top: 242px;
    width: 550px;
    height: 315px;
    background: var(--kraft);
    overflow: hidden;
    box-shadow: 0 6px 18px rgba(0,0,0,0.12);
  }
  .card--front { left: 35px; }
  .card--back { left: 615px; }

  .brand {
    position: absolute;
    display: flex;
    align-items: center;
    gap: 12px;
  }
  .brand__dot {
    width: 34px; height: 34px;
    border-radius: 50%;
    background: var(--leaf-green);
  }
  .brand__name {
    font-family: "Roboto", Arial, sans-serif;
    font-weight: 700;
    color: var(--ink);
    letter-spacing: 1px;
    white-space: nowrap;
  }
  .card--front .brand { left: 52px; top: 138px; }
  .card--front .brand__name { font-size: 36px; }
  .card--back .brand { left: 40px; top: 132px; }
  .card--back .brand__dot { width: 28px; height: 28px; }
  .card--back .brand__name { font-size: 28px; }

  .motif {
    position: absolute;
    right: -40px; top: -30px;
    width: 260px; height: 300px;
    border-radius: 50%;
    background: radial-gradient(circle at 45% 45%, rgba(185,220,60,0.55), rgba(76,175,63,0.35) 55%, rgba(216,213,208,0) 72%);
  }

  .back-shape { position: absolute; inset: 0; }

  .contact {
    position: absolute;
    left: 342px; top: 72px;
    color: var(--white);
  }
  .contact__name {
    font-size: 16px;
    font-weight: 500;
    color: var(--lime-text);
  }
  .contact__role {
    font-size: 11px;
    margin-top: 2px;
  }
  .contact__list {
    list-style: none;
    margin-top: 26px;
  }
  .contact__item {
    display: flex;
    align-items: flex-start;
    gap: 9px;
    font-size: 12px;
    line-height: 16px;
    margin-bottom: 9px;
  }
  .contact__icon {
    flex: 0 0 16px;
    width: 16px; height: 16px;
  }
</style>
</head>
<body>

<section class="card card--front" aria-label="Card front">
  <div class="motif" role="img" aria-label="Large brand motif in green tones"></div>
  <div class="brand">
    <span class="brand__dot"></span>
    <span class="brand__name">Tolvin Waste</span>
  </div>
</section>

<section class="card card--back" aria-label="Card back">
  <svg class="back-shape" viewBox="0 0 550 315" preserveAspectRatio="none" aria-hidden="true">
    <path d="M292 0 C318 110 300 220 226 315 L550 315 L550 0 Z" fill="var(--lime)"/>
    <path d="M318 0 C340 115 322 225 252 315 L550 315 L550 0 Z" fill="var(--leaf-green)"/>
  </svg>

  <div class="brand">
    <span class="brand__dot"></span>
    <span class="brand__name">Tolvin Waste</span>
  </div>

  <div class="contact">
    <p class="contact__name">Marlow Keating</p>
    <p class="contact__role">Manager</p>
    <ul class="contact__list">
      <li class="contact__item">
        <svg class="contact__icon" viewBox="0 0 16 16" aria-hidden="true"><circle cx="8" cy="8" r="8" fill="var(--icon-disc)"/><path d="M5.2 4.2l1.6-.4 1 2-1 .8c.5 1 1.3 1.8 2.3 2.3l.8-1 2 1-.4 1.6c-3.4.2-6.5-2.9-6.3-6.3z" fill="var(--icon-glyph)"/></svg>
        <span>0871 22 64 19</span>
      </li>
      <li class="contact__item">
        <svg class="contact__icon" viewBox="0 0 16 16" aria-hidden="true"><circle cx="8" cy="8" r="8" fill="var(--icon-disc)"/><rect x="4" y="5.2" width="8" height="5.6" rx=".6" fill="var(--icon-glyph)"/><path d="M4.3 5.6L8 8.4l3.7-2.8" stroke="var(--icon-disc)" stroke-width=".8" fill="none"/></svg>
        <span>info@tolvinwaste.com</span>
      </li>
      <li class="contact__item">
        <svg class="contact__icon" viewBox="0 0 16 16" aria-hidden="true"><circle cx="8" cy="8" r="8" fill="var(--icon-disc)"/><circle cx="8" cy="8" r="4" fill="none" stroke="var(--icon-glyph)" stroke-width="1"/><ellipse cx="8" cy="8" rx="1.8" ry="4" fill="none" stroke="var(--icon-glyph)" stroke-width=".8"/><path d="M4 8h8" stroke="var(--icon-glyph)" stroke-width=".8"/></svg>
        <span>www.tolvinwaste.com</span>
      </li>
      <li class="contact__item">
        <svg class="contact__icon" viewBox="0 0 16 16" aria-hidden="true"><circle cx="8" cy="8" r="8" fill="var(--icon-disc)"/><path d="M8 12.5S4.8 9 4.8 7a3.2 3.2 0 016.4 0c0 2-3.2 5.5-3.2 5.5z" fill="var(--icon-glyph)"/><circle cx="8" cy="7" r="1.1" fill="var(--icon-disc)"/></svg>
        <span>No. 4127, birchwood lane<br>springfield 402</span>
      </li>
    </ul>
  </div>
</section>

</body>
</html>
```